Our company TrulaPay, an online processor of payments is seeking talented submissions for our website redesign. The winning design will be chopped up and converted into a WordPress theme to allow for easy content additions and updates.

We are looking for modern designs that rival current websites in our industry (plimo.example, zanquetto.example, holvix.example, brandle.example, quillmarkcharges.example, evensplitcharges.example, KoboRun.example).

Our company is seeking to expand our reach to software developers and engineers who are either integrating our payment platform into their offerings or are engineering a custom solution for the company they work for and are in need of a payment platform such as our own.

We currently work with hundreds of different business partners whom either resell our services or integrate our processing capabilities into their software (which they sell). We also must communicate effectively to end users, businesses, who seek us out directly for their payment processing needs.

We are open to different color schemes but would ultimately like them to be somewhat inline with our current logo (see attached). Our website needs to instill security and confidence to any current and/or potential user as we are trusted with private and sensitive information.

We are seeking submissions from qualified; individual freelancers, freelance teams, and agencies who can attack this project in its entirety. Since this project is a total redesign, we would like submissions that have the capability to design any custom graphics, icons, buttons, and illustrations in line with our industry, capabilities, offerings, and content. We are looking for someone to design our new website and would prefer a vendor who can also help us to design elements (graphics, illustrations, charts, workflows) within our website.

Designs will be converted into a wordpress theme and we would like to utilize widgets for as many areas as possible to make editing and updating easy.

We are seeking the creation of a few unique pages but many of the pages for the majority of our content will just be internal content pages which will be duplicated.

We will likely contract with the winning submission for future work.

Please see Design Reference Document for more information

Target Market(s)

Resellers
Merchant Service Providers
Software Developers
Independent Sales Organizations (ISOs)
App Builders
Mobile App Builders
Independent Software Developers
Organizational Software Developers
Businesses who need to accept payments
Governments
Municipalities
Schools
DMVs
Courts
Retailers
Medical Offices
Hosipitals
Clinics
Dr. Offices
Gyms
Churches
Non-Profits
Software Companies
Technology Companies
Startups

• Logo cannot change drastically.

```html
<!DOCTYPE html>
<html lang="en">
<head>
<meta charset="utf-8">
<title>TrulaPay — Payment Processing</title>
<link rel="stylesheet" href="https://fonts.googleapis.com/css2?family=Oswald:wght@400;500&family=Ubuntu:wght@400;500&display=swap">
<style>
:root{
  --red:#d70f0f;
  --navy:#1a1a8c;
  --blue:#1212b8;
  --link:#1f2bb0;
  --ink:#222;
  --text:#333;
  --muted:#666;
  --page:#f6f6f6;
  --band:#ebebeb;
  --white:#fff;
}
*{box-sizing:border-box;margin:0;padding:0}
html,body{width:1006px;height:1200px;overflow:hidden}
body{position:relative;background:var(--page);font-family:"Ubuntu",Arial,sans-serif;color:var(--text)}
.abs{position:absolute}

.top-rule{left:0;top:0;width:1006px;height:2px;background:var(--red)}
.contact-tab{left:640px;top:0;width:248px;height:29px;background:var(--red);color:var(--white);
  font-size:11px;font-weight:500;display:flex;align-items:center;justify-content:center;
  clip-path:polygon(0 0,100% 0,97% 100%,3% 100%)}
.brand{left:120px;top:30px;font-size:36px;color:var(--navy);font-weight:400;letter-spacing:-.5px;display:flex;align-items:center;gap:8px}
.brand i{display:block;width:10px;height:10px;border-radius:50%;background:var(--red)}

.main-nav{left:0;top:107px;width:1006px;height:34px;background:linear-gradient(#ececec,#dcdcdc);border-top:1px solid #cfcfcf;border-bottom:1px solid #c4c4c4}
.main-nav ul{list-style:none;display:flex;position:absolute;left:114px;top:0;height:33px}
.main-nav li{font-size:12.5px;font-weight:500;color:var(--ink);padding:0 14px;line-height:33px;border-right:1px solid #c6c6c6}
.main-nav li:last-child{border-right:none}
.main-nav li.current{color:var(--navy)}
.search{left:668px;top:3px;width:220px;height:27px;background:var(--white);border:1px solid #d0d0d0;font-size:12px;color:#9a9a9a;padding:0 12px;line-height:25px}
.search svg{position:absolute;right:10px;top:3px}

.hero{left:0;top:141px;width:1006px;height:392px;background:radial-gradient(ellipse at 50% 40%,#f2f2f2,#d6d6d6)}
.frame{top:72px;width:322px;height:247px;background:var(--white);padding:4px;box-shadow:0 2px 6px rgba(0,0,0,.15)}
.frame div{width:100%;height:100%}
.frame-team{left:142px}.frame-team div{background:linear-gradient(135deg,#e8e8e8,#9a9ca2 60%,#3d3f48)}
.frame-code{left:474px}.frame-code div{background:linear-gradient(135deg,#0a0a14,#1b2c6a 55%,#050508)}
.cta{top:331px;width:204px;height:46px;border-radius:5px;color:var(--white);font-family:"Oswald",sans-serif;font-weight:500;font-size:20px;
  display:flex;align-items:center;justify-content:center;border:4px solid #e4e4e4;box-shadow:0 8px 8px -6px rgba(0,0,0,.35);text-shadow:0 1px 1px rgba(0,0,0,.4)}
.cta-business{left:205px;background:linear-gradient(#f2302a,#c80707)}
.cta-devs{left:534px;background:linear-gradient(#2a2ad0,#0a0a8a)}

.section-title{font-family:"Oswald",sans-serif;font-weight:400;font-size:26px;color:#3a3a3a;letter-spacing:-.3px}
.welcome-title{left:126px;top:556px}
.welcome-text{left:126px;top:598px;width:470px;font-size:10px;line-height:15.2px;color:var(--ink)}
.welcome-text p{margin-bottom:8px}
.read-more{left:126px;top:773px;font-size:10.5px;font-weight:500;color:#555}

.solutions-title{left:640px;top:556px}
.solutions-panel{left:658px;top:604px;width:194px;height:180px;background:linear-gradient(90deg,#fff,#f0f0f0);box-shadow:0 3px 6px rgba(0,0,0,.12);border-radius:0 18px 18px 0}
.solutions-panel ul{list-style:none;padding:6px 0 0 10px}
.solutions-panel li{position:relative;height:24.6px;line-height:24.6px;font-size:10px;color:var(--link);padding-left:18px;border-bottom:1px solid #e0e0e0;width:142px}
.solutions-panel li:last-child{border-bottom:none}
.solutions-panel svg{position:absolute;left:0;top:5px}

.ach{left:0;top:804px;width:1006px;height:296px;background:var(--band);border-top:1px solid #e0e0e0}
.ach-title{left:0;top:8px;width:1006px;text-align:center}
.divider{left:344px;top:53px;width:316px;height:1px;background:#cfcfcf}
.divider-dots{left:484px;top:47px}
.card{top:75px;width:232px;height:198px;background:linear-gradient(#f4f4f4,#e2e2e2);border:1px solid #9a9a9a;box-shadow:0 10px 8px -8px rgba(0,0,0,.35)}
.card-tab{position:absolute;top:-4px;left:50%;transform:translateX(-50%);padding:0 6px;height:34px;line-height:34px;background:linear-gradient(#fff,#ececec);
  border:1px solid #bdbdbd;border-top:none;border-radius:0 0 3px 3px;font-family:"Oswald",sans-serif;font-weight:400;font-size:12px;color:var(--blue);white-space:nowrap}
.card-media{position:absolute;left:4px;top:34px;width:222px;height:98px}
.card p{position:absolute;left:4px;top:134px;width:222px;height:58px;background:var(--white);border-top:1px dashed #bbb;border-bottom:1px dashed #bbb;
  font-size:11px;line-height:16px;color:var(--muted);text-align:center;padding-top:4px}
.card-gateway{left:126px}.card-gateway .card-media{background:linear-gradient(135deg,#6b6e78,#d9b27a 55%,#2c2e36)}
.card-api{left:388px}.card-api .card-media{background:linear-gradient(100deg,#3bb23b,#8fde6a 55%,#e8e8e8)}
.card-dev{left:648px}.card-dev .card-media{background:linear-gradient(90deg,#fbfbfb,#efe6e0 70%,#d9c3b4)}

.site-footer{left:0;top:1100px;width:1006px;height:100px;background:var(--white);border-top:1px solid #e2e2e2}
.contact-line{left:128px;font-size:11px;color:#555;line-height:16px}
.contact-line span{position:absolute;left:26px;white-space:nowrap}
.social{left:790px;font-size:11px;color:#555;display:flex;align-items:center;gap:14px}
.social i{display:block;width:18px;height:18px;border-radius:50%;background:#555}
</style>
</head>
<body>
<div class="abs top-rule"></div>
<div class="abs contact-tab">Call us on (555) 014-2290 | email us | login</div>
<div class="abs brand">TrulaPay<i></i></div>

<nav class="abs main-nav">
  <ul>
    <li class="current">Home</li><li>Solutions</li><li>Developers</li><li>Partners</li><li>Company</li><li>Resources</li><li>Blog</li>
  </ul>
  <div class="abs search">Search
    <svg width="20" height="20" viewBox="0 0 20 20"><circle cx="9" cy="9" r="7" fill="none" stroke="#999" stroke-width="1.5"/><line x1="14" y1="14" x2="19" y2="19" stroke="#999" stroke-width="1.5"/></svg>
  </div>
</nav>

<section class="abs hero">
  <div class="abs frame frame-team"><div role="img" aria-label="Photo of a business team meeting around a table"></div></div>
  <div class="abs frame frame-code"><div role="img" aria-label="Photo of blue source code on a dark screen"></div></div>
  <div class="abs cta cta-business">Businesses Click Here</div>
  <div class="abs cta cta-devs">Devs Click Here</div>
</section>

<h2 class="abs section-title welcome-title">Welcome</h2>
<div class="abs welcome-text">
  <p>Lorem ipsum dolor sit amet, consectetuer adipiscing elit, sed diam nonummy nibh euismod tincidunt ut laoreet dolore magna aliquam erat volutpat. Ut wisi enim ad minim veniam, quis nostrud exerci tation ullamcorper suscipit lobortis nisl ut aliquip ex ea commodo consequat. Duis autem vel eum iriure dolor in hendrerit in vulputate velit esse molestie consequat, vel illum dolore eu feugiat nulla facilisis at vero eros et accumsan et iusto odio dignissim qui blandit praesent luptatum zzril delenit augue duis dolore</p>
  <p>Lorem ipsum dolor sit amet, consectetuer adipiscing elit, sed diam nonummy nibh euismod tincidunt ut laoreet dolore magna aliquam erat volutpat. Ut wisi enim ad minim veniam, quis nostrud exerci tation ullamcorper suscipit lobortis nisl ut aliquip ex ea commodo consequat. Duis autem vel eum iriure dolor in hendrerit in vulputate velit esse molestie consequat, vel illum dolore eu feugiat nulla facilisis at vero eros et accumsan et iusto odio</p>
</div>
<div class="abs read-more">Read More +</div>

<h2 class="abs section-title solutions-title">Custom Industry Solutions</h2>
<div class="abs solutions-panel">
  <ul>
    <li><svg width="13" height="13" viewBox="0 0 13 13"><path d="M1 7 L5 12 L12 1" fill="none" stroke="#d70f0f" stroke-width="2"/></svg>Custom Industry Solutions</li>
    <li><svg width="13" height="13" viewBox="0 0 13 13"><path d="M1 7 L5 12 L12 1" fill="none" stroke="#d70f0f" stroke-width="2"/></svg>Government</li>
    <li><svg width="13" height="13" viewBox="0 0 13 13"><path d="M1 7 L5 12 L12 1" fill="none" stroke="#d70f0f" stroke-width="2"/></svg>Medical</li>
    <li><svg width="13" height="13" viewBox="0 0 13 13"><path d="M1 7 L5 12 L12 1" fill="none" stroke="#d70f0f" stroke-width="2"/></svg>Fitness</li>
    <li><svg width="13" height="13" viewBox="0 0 13 13"><path d="M1 7 L5 12 L12 1" fill="none" stroke="#d70f0f" stroke-width="2"/></svg>Martial Arts</li>
    <li><svg width="13" height="13" viewBox="0 0 13 13"><path d="M1 7 L5 12 L12 1" fill="none" stroke="#d70f0f" stroke-width="2"/></svg>Alarm Monitoring</li>
    <li><svg width="13" height="13" viewBox="0 0 13 13"><path d="M1 7 L5 12 L12 1" fill="none" stroke="#d70f0f" stroke-width="2"/></svg>Property Management</li>
  </ul>
</div>

<section class="abs ach">
  <h2 class="abs section-title ach-title">ACH Payment Processing</h2>
  <div class="abs divider"></div>
  <svg class="abs divider-dots" width="40" height="14" viewBox="0 0 40 14"><rect x="0" y="0" width="40" height="14" fill="#ebebeb"/><circle cx="5" cy="7" r="3" fill="#ccc"/><circle cx="20" cy="7" r="6" fill="#fff" stroke="#bbb" stroke-width="2"/><circle cx="20" cy="7" r="3" fill="#bbb"/><circle cx="35" cy="7" r="3" fill="#ccc"/></svg>

  <article class="abs card card-gateway">
    <h3 class="card-tab">PAYMENT GATEWAY</h3>
    <div class="card-media" role="img" aria-label="Photo of a hand holding a payment card over a keyboard"></div>
    <p>Lorem ipsum dolor sit amet, consectetuer adipiscing elit, sed diam nonummy nibh euismod tincidunt ut laoreet dolore.</p>
  </article>
  <article class="abs card card-api">
    <h3 class="card-tab">ACH PAYMENT API</h3>
    <div class="card-media" role="img" aria-label="Illustration of a secure address bar with a cursor arrow"></div>
    <p>Lorem ipsum dolor sit amet, consectetuer adipiscing elit, sed diam nonummy nibh euismod tincidunt ut laoreet dolore.</p>
  </article>
  <article class="abs card card-dev">
    <h3 class="card-tab">PROCESSING FOR SOFTWARE DEVELOPMENT</h3>
    <div class="card-media" role="img" aria-label="Photo of a hand sketching a success diagram on glass"></div>
    <p>Lorem ipsum dolor sit amet, consectetuer adipiscing elit, sed diam nonummy nibh euismod tincidunt ut laoreet dolore.</p>
  </article>
</section>

<footer class="abs site-footer">
  <div class="abs contact-line" style="top:12px">
    <svg width="12" height="16" viewBox="0 0 12 16"><path d="M6 0 C2.7 0 0 2.6 0 5.8 C0 10 6 16 6 16 S12 10 12 5.8 C12 2.6 9.3 0 6 0Z" fill="#333"/><circle cx="6" cy="5.8" r="2.2" fill="#fff"/></svg>
    <span style="top:-2px">Lorem ipsum dolor sit amet,<br>consectetuer adipiscing elit</span>
  </div>
  <div class="abs contact-line" style="top:48px">
    <svg width="12" height="12" viewBox="0 0 12 12"><path d="M2 0 L4.5 0 L5.5 3 L4 4.5 C4.8 6.3 5.7 7.2 7.5 8 L9 6.5 L12 7.5 L12 10 C12 11 11 12 10 12 C4.5 12 0 7.5 0 2 C0 1 1 0 2 0Z" fill="#333"/></svg>
    <span style="top:-3px">(555) 014-2290</span>
  </div>
  <div class="abs contact-line" style="top:74px">
    <svg width="13" height="10" viewBox="0 0 13 10"><rect width="13" height="10" fill="#333"/><path d="M0 0 L6.5 5.5 L13 0" fill="none" stroke="#fff" stroke-width="1.2"/></svg>
    <span style="top:-4px">support@trulapay.example</span>
  </div>

  <div class="abs social" style="top:8px"><i></i>Friendlane</div>
  <div class="abs social" style="top:40px"><i></i>Chirpline</div>
  <div class="abs social" style="top:72px"><i></i>Workweave</div>
</footer>
</body>
</html>
```